Stationary design for boutique production house

We need a stationary design for our production house, 'Luma Studios' based in Singapore. We produce microfilms as well as podcasts, talkshows and events. Our logo is a stylized icon of our director, who is also the executive producer and host of our programs, Orla. Our main company colors are Red, Black and white. We would like a clean, minimalist design incorporating our existing company logo that conveys a sense of urbanism and elegance.

Logo and font files are attached. f

Target Market(s)

We focus on lifestyle media rather than entertainment.

Industry/Entity Type

Boutique

Font styles to use
Serif
Sans Serif

Colors
ec1f27
ffffff
000000

Requirements
Must have
• Our company logo and at least one of our company colors.
Nice to have
• Our address and contact information.
Should not have
• Changes made to the company logo (using only certain parts of it is fine though)

```html
<!DOCTYPE html>
<html lang="en">
<head>
<meta charset="utf-8">
<title>Luma Studios — Stationery</title>
<link rel="stylesheet" href="https://fonts.googleapis.com/css2?family=Tinos:wght@400;700&family=Open+Sans:wght@400;600&display=swap">
<style>
  :root {
    --brand-red: #d91c22;
    --brand-red-deep: #bf141a;
    --ink: #1a1a1a;
    --paper: #ffffff;
    --backdrop: #e6e6e6;
    --muted: #666666;
    --rule: #9a9a9a;
  }
  * { box-sizing: border-box; margin: 0; padding: 0; }
  html, body { width: 1200px; height: 703px; overflow: hidden; background: var(--backdrop); }
  body { position: relative; font-family: "Open Sans", sans-serif; color: var(--ink); }

  .sheet { position: absolute; background: var(--paper); box-shadow: 0 1px 1.5px rgba(0,0,0,0.25); }

  .brand-name { font-family: "Tinos", serif; font-weight: 700; text-align: center; line-height: 1.05; letter-spacing: 0.02em; }

  /* Presentation folder */
  .folder { position: absolute; left: 126px; top: 134px; width: 291px; height: 397px; background: var(--brand-red); }
  .folder .brand-name { position: absolute; left: 0; right: 0; top: 328px; color: var(--brand-red-deep); font-size: 21px; font-weight: 400; }
  .folder .brand-dot { position: absolute; left: 139px; top: 296px; width: 13px; height: 13px; border-radius: 50%; background: var(--brand-red-deep); }

  /* Letterhead */
  .letterhead { left: 454px; top: 138px; width: 271px; height: 385px; }
  .logo-block { position: absolute; background: var(--brand-red); display: flex; align-items: flex-end; justify-content: center; padding-bottom: 6px; }
  .logo-block .brand-name { color: var(--paper); }
  .letterhead .logo-block { left: 20px; top: 0; width: 50px; height: 56px; }
  .letterhead .logo-block .brand-name { font-size: 6px; font-weight: 400; }
  .contact-stack { position: absolute; left: 194px; top: 22px; padding-left: 5px; border-left: 0.6px solid var(--rule); font-family: "Tinos", serif; font-weight: 700; font-size: 3.4px; line-height: 4.3px; color: var(--ink); }
  .contact-stack .icon { display: inline-block; width: 2.4px; height: 2.4px; border-radius: 50%; background: var(--brand-red); margin-right: 1.5px; vertical-align: middle; }
  .letter-body { position: absolute; left: 20px; top: 131px; width: 226px; }
  .letter-title { font-size: 5.4px; color: #444; line-height: 7px; }
  .letter-date { font-size: 3.8px; color: #555; line-height: 5px; margin-bottom: 6px; }
  .letter-body p { font-size: 3.9px; line-height: 6.4px; color: #555; text-indent: 8px; text-align: justify; margin-bottom: 6.5px; }
  .letter-body p + p { margin-top: 0; }
  .letter-body p.gap { margin-top: 9px; }
  .seal { position: absolute; left: 196px; top: 302px; width: 40px; height: 36px; }

  /* Envelopes */
  .envelope-front { left: 762px; top: 134px; width: 289px; height: 144px; }
  .envelope-front .logo-block { left: 14px; top: 0; width: 48px; height: 55px; }
  .envelope-front .logo-block .brand-name { font-size: 5.6px; font-weight: 400; }
  .return-address { position: absolute; left: 14px; top: 60px; width: 48px; text-align: center; font-family: "Tinos", serif; font-weight: 700; font-size: 3.3px; line-height: 4.6px; color: #444; }
  .envelope-back { left: 762px; top: 296px; width: 289px; height: 143px; }
  .envelope-back .flap { position: absolute; inset: 0; width: 100%; height: 100%; }
  .envelope-back .brand-name { position: absolute; left: 0; right: 0; top: 321px; font-size: 4.5px; }
  .envelope-back .mark { position: absolute; top: 14px; left: 0; right: 0; text-align: center; }
  .envelope-back .mark .brand-name { position: static; color: var(--ink); font-size: 6px; }
  .envelope-back .mark .brand-dot { display: inline-block; width: 4px; height: 4px; border-radius: 50%; background: var(--brand-red); margin-bottom: 2px; }

  /* Business cards */
  .card { position: absolute; top: 465px; width: 98px; height: 170px; box-shadow: 0 1px 1.5px rgba(0,0,0,0.25); }
  .card-front { left: 802px; background: var(--brand-red); color: var(--paper); }
  .card-front .brand-name { position: absolute; left: 0; right: 0; top: 52px; font-size: 7.4px; font-weight: 400; }
  .card-front .brand-dot { position: absolute; left: 45px; top: 36px; width: 8px; height: 8px; border-radius: 50%; background: var(--paper); }
  .card-front .holder { position: absolute; left: 0; right: 0; top: 97px; text-align: center; font-family: "Tinos", serif; font-weight: 700; }
  .holder .name { font-size: 6.2px; letter-spacing: 0.04em; }
  .holder .title { font-size: 4.2px; margin-top: 1.5px; }
  .card-front .divider { position: absolute; left: 16px; right: 16px; top: 113px; height: 0.6px; background: var(--paper); }
  .card-front .divider-dot { position: absolute; left: 46px; top: 110.5px; width: 5.5px; height: 5.5px; border-radius: 50%; background: var(--paper); }
  .card-front .details { position: absolute; left: 0; right: 0; top: 119px; text-align: center; font-family: "Tinos", serif; font-weight: 700; font-size: 4px; line-height: 5.5px; }
  .card-front .details .spacer { height: 3px; }
  .card-front .bottom-rule { position: absolute; left: 16px; right: 16px; top: 156px; height: 0.6px; background: var(--paper); }
  .card-back { left: 913px; background: var(--paper); }
  .card-back .brand-dot { position: absolute; left: 45px; top: 77px; width: 8px; height: 8px; border-radius: 50%; background: var(--brand-red); }
  .card-back .brand-name { position: absolute; left: 0; right: 0; top: 94px; color: var(--ink); font-size: 8px; font-weight: 400; }
  .card-back .brand-name .accent { color: var(--ink); }
</style>
</head>
<body>

  <!-- Presentation folder -->
  <section class="folder" aria-label="Presentation folder">
    <span class="brand-dot"></span>
    <div class="brand-name">LUMA<br>STUDIOS</div>
  </section>

  <!-- Letterhead -->
  <section class="sheet letterhead" aria-label="Letterhead">
    <div class="logo-block"><div class="brand-name">LUMA<br>STUDIOS</div></div>
    <address class="contact-stack">
      Street Address Line 1<br>
      Your City, Postal Code<br>
      <span class="icon"></span>+00 (0)00 0000<br>
      <span class="icon"></span>+00 (0)00 0000<br>
      <span class="icon"></span>info@lumastudios.com<br>
      <span class="icon"></span>www.lumastudios.com
    </address>
    <div class="letter-body">
      <div class="letter-title">Luma Studios</div>
      <div class="letter-date">December 22, 2014/Revised February 2, 2015</div>
      <p>Lorem ipsum dolor sit amet, consectetur adipiscing elit. Sed libero est, pellentesque facilisis tempor eu, pulvinar vitae justo. Praesent bibendum ultricies magna luctus luctus. Suspendisse potenti. Pellentesque habitant morbi tristique senectus et netus et malesuada fames ac turpis egestas. Nullam elit urna, porttitor quis luctus ac, gravida in ante. Vestibulum ante ipsum primis in faucibus orci luctus et ultrices posuere cubilia curae.</p>
      <p>Donec consectetur tempor purus. Nullam turpis lacus, molestie bibendum auctor non, convallis quis mauris. Cum sociis natoque penatibus et magnis dis parturient montes, nascetur ridiculus mus. Aenean feugiat erat sit amet massa semper ullamcorper. Fusce turpis nunc, pellentesque quis accumsan viverra, tempor vel sem. Etiam varius, velit et pretium cursus, lorem massa consequat orci, sit amet interdum turpis nibh ac eros.</p>
      <p class="gap">Nam et tellus nulla, eget congue nisl. Mauris dui tortor, quis scelerisque velit. Sed pretium blandit odio, vel malesuada purus convallis vitae. Aliquam erat volutpat. Donec consectetur tempor purus, nullam turpis lacus molestie bibendum auctor non, convallis quis mauris ut dictum tellus.</p>
    </div>
    <svg class="seal" viewBox="0 0 40 36" role="img" aria-label="Signature and company seal">
      <circle cx="22" cy="18" r="15" fill="#e9e9f0"/>
    </svg>
  </section>

  <!-- Envelope, front -->
  <section class="sheet envelope-front" aria-label="Envelope front">
    <div class="logo-block"><div class="brand-name">LUMA<br>STUDIOS</div></div>
    <address class="return-address">Street Address Line 1<br>Your City, Postal Code</address>
  </section>

  <!-- Envelope, back -->
  <section class="sheet envelope-back" aria-label="Envelope back">
    <svg class="flap" viewBox="0 0 289 143" preserveAspectRatio="none" aria-hidden="true">
      <polyline points="0,0 30,46 259,46 289,0" fill="none" stroke="#e2e2e2" stroke-width="0.8"/>
    </svg>
    <div class="mark">
      <span class="brand-dot"></span>
      <div class="brand-name">LUMA STUDIOS</div>
    </div>
  </section>

  <!-- Business card, front -->
  <section class="card card-front" aria-label="Business card front">
    <span class="brand-dot"></span>
    <div class="brand-name">LUMA<br>STUDIOS</div>
    <div class="holder">
      <div class="name">ORLA REYES</div>
      <div class="title">President</div>
    </div>
    <div class="divider"></div>
    <span class="divider-dot"></span>
    <div class="details">
      Street Address Line 1<br>
      Your City, Postal Code<br>
      <div class="spacer"></div>
      T: +00 (0)00 0000<br>
      F: +00 (0)00 0000<br>
      E: info@lumastudios.com<br>
      www.lumastudios.com
    </div>
    <div class="bottom-rule"></div>
  </section>

  <!-- Business card, back -->
  <section class="card card-back" aria-label="Business card back">
    <span class="brand-dot"></span>
    <div class="brand-name">LUMA<br>STUDIOS</div>
  </section>

</body>
</html>
```